TRN marine wildlife conservation strategy

The Harbourline Stewardship Union (trn-stewards.org) needs an illustration to explain in a captivating and clear fashion the influences and interactions underlying our marine wildlife conservation planning and policymaking process. This will be included in our forthcoming strategy paper, and widely presented in conferences. Ultimately, this illustration will help governments take the right decisions to protect wildlife and natural resources.
Guidelines:
Size: The illustration shall fit in a A4 page, and also render nicely on a projector screen (1920x1080)
Colors: Avoid too colorful and 'playful' color code
Text: - Case shall be consistent throughout the graphic (unlike the draft design provided)
Graphic elements:
- In the top right of the graphic there is supposed to be a map of Myanmar. The map is attached. Feel free to adjust the map colors and style to match the illustration.
The only key areas we shall include in the map are:
- Myanmar borders
- EEZ (green),
- state/region borders (dotted lines),
- two marine corridors (blue and light red).
Everything else shall be left out (such as minimap, legend, scale, compass, SEZ).
- On the bottom right, it's important for the national benefits to be presented as a Venn diagram like in the original draft illustration (three intersecting circles)
Any questions? Please ask: mpaley@trn-stewards.org
Thank you!
Target Market(s)
Scientists, policy makers.
Industry/Entity Type
Environment

```html
<!DOCTYPE html>
<html lang="en">
<head>
<meta charset="utf-8">
<title>Spatial Management Plan – Harbourline Stewardship Union</title>
<link rel="stylesheet" href="https://fonts.googleapis.com/css2?family=Graduate&family=Montserrat:wght@300;500;600&display=swap">
<style>
  :root{
    --sky:#5bb5ef;
    --sky-dark:#3f9fdd;
    --ink:#111111;
    --arrow:#4b4b4d;
    --orange:#d98a4a;
    --orange-tint:#c78656;
    --green:#86bd82;
    --green-tint:#9fc99a;
    --stone:#d9d9db;
    --stone-tint:#c8c9cc;
    --hub:#dcdde0;
    --hex:#82b77c;
    --label:#555555;
    --white:#ffffff;
  }
  html,body{margin:0;padding:0;width:1200px;height:953px;overflow:hidden;background:#8f8f92;}
  .plan{display:block;width:1200px;height:953px;}
  .heading{font-family:"Graduate",serif;fill:var(--ink);letter-spacing:.5px;}
  .body-text{font-family:"Montserrat",sans-serif;fill:#1e1e1e;font-weight:500;}
  .engage{font-family:"Montserrat",sans-serif;font-weight:300;fill:var(--label);font-size:12.5px;letter-spacing:.5px;}
  .callout{fill:var(--sky);}
  .callout-line{fill:none;stroke:var(--white);stroke-width:1.5;}
  .flow-arrow{fill:none;stroke:var(--arrow);stroke-width:22;}
  .flow-head{fill:var(--arrow);}
  .hex-cell{fill:var(--hex);stroke:#4d8a52;stroke-width:1;}
  .hex-dash{fill:none;stroke:#3c6e42;stroke-width:1;stroke-dasharray:4 3;}
  .seg-orange{fill:var(--orange);}
  .seg-stone{fill:var(--stone);}
  .seg-green{fill:var(--green);}
  .tint-orange{fill:var(--orange-tint);}
  .tint-stone{fill:var(--stone-tint);}
  .tint-green{fill:var(--green-tint);}
  .cycle-band{fill:none;stroke:var(--sky);stroke-width:30;}
  .cycle-dash{fill:none;stroke:var(--white);stroke-width:1.5;stroke-dasharray:6 4;}
  .cycle-head{fill:var(--sky);}
  .hub{fill:var(--hub);}
  .venn-eco{fill:var(--orange);}
  .venn-soc{fill:var(--green);}
  .venn-env{fill:var(--stone);}
  .venn-overlap{fill:var(--sky);}
  .venn-dash{fill:none;stroke:var(--sky-dark);stroke-width:1.2;stroke-dasharray:5 4;}
  .adapt-band{fill:none;stroke:var(--arrow);stroke-width:30;}
  .adapt-text{font-family:"Montserrat",sans-serif;font-weight:600;fill:var(--white);font-size:14px;letter-spacing:1px;}
</style>
</head>
<body>
<svg class="plan" viewBox="0 0 1410 997" preserveAspectRatio="none" xmlns="http://www.w3.org/2000/svg">
  <defs>
    <linearGradient id="backdrop" x1="0" y1="0" x2="0" y2="1">
      <stop offset="0" stop-color="#f6f6f6"/>
      <stop offset="0.55" stop-color="#d4d4d6"/>
      <stop offset="1" stop-color="#9c9c9e"/>
    </linearGradient>
    <linearGradient id="mapTone" x1="0" y1="0" x2="1" y2="1">
      <stop offset="0" stop-color="#ffffff"/>
      <stop offset="0.6" stop-color="#e4e6ea"/>
      <stop offset="1" stop-color="#c7cfd8"/>
    </linearGradient>
    <polygon id="hexOuter" points="0,-62 53.7,-31 53.7,31 0,62 -53.7,31 -53.7,-31"/>
    <polygon id="hexInner" points="0,-54 46.8,-27 46.8,27 0,54 -46.8,27 -46.8,-27"/>
    <clipPath id="clipSoc"><circle cx="1130" cy="754" r="97"/></clipPath>
    <clipPath id="clipEnv"><circle cx="1295" cy="747" r="97"/></clipPath>

    <path id="arcConsensus1" d="M549.6 254.3 A262 262 0 0 1 976.1 409.4"/>
    <path id="arcConsensus2" d="M568.8 277.3 A232 232 0 0 1 946.5 414.6"/>
    <path id="arcInst1" d="M971.1 387.1 A262 262 0 0 1 650.1 708.1"/>
    <path id="arcInst2" d="M942.1 394.9 A232 232 0 0 1 657.9 679.1"/>
    <path id="arcData" d="M675.4 696.3 A245 245 0 0 1 560.5 267.3"/>
    <path id="arcEngStone" d="M631.8 344.7 A140 140 0 0 1 846.9 400.3"/>
    <path id="arcEngOrange" d="M684.1 590.8 A140 140 0 0 1 610.8 365.0"/>
    <path id="arcEngGreen" d="M854.9 425.9 A140 140 0 0 1 705.8 594.5"/>
    <path id="arcTop" d="M633.7 384.3 A110 110 0 0 1 802.3 384.3"/>
    <path id="arcRight" d="M820.0 413.8 A110 110 0 0 1 737.1 563.4"/>
    <path id="arcLeft" d="M702.7 563.9 A110 110 0 0 1 614.6 417.4"/>
    <path id="arcBenefits" d="M1020 800 A215 215 0 0 1 1232 520"/>
    <path id="pathAdaptive" d="M1030 330 Q1085 305 1140 350"/>
    <path id="pathManagement" d="M1020 375 Q1070 420 1130 395"/>
  </defs>

  <rect class="backdrop" x="0" y="0" width="1410" height="997" fill="url(#backdrop)"/>

  <!-- Map area -->
  <rect class="region-map" x="1162" y="58" width="232" height="442" rx="6" fill="url(#mapTone)" role="img"
        aria-label="Map of Myanmar with national borders, EEZ, dotted state and region borders and two marine corridors"/>

  <!-- Title -->
  <text class="heading plan-title" x="1388" y="36" text-anchor="end" font-size="23">SPATIAL MANAGEMENT PLAN</text>

  <!-- Pressure callouts -->
  <g class="pressure political">
    <path class="callout" d="M270 17 H503 A55 55 0 0 1 558 72 V147 H325 A55 55 0 0 1 270 92 Z"/>
    <path class="callout-line" d="M294 31 H498 A46 46 0 0 1 544 77 V133 H332 A46 46 0 0 1 286 87 V31 Z"/>
    <text class="heading" x="414" y="91" text-anchor="middle" font-size="19">POLITICAL TRANSITION</text>
  </g>

  <g class="pressure development">
    <path class="callout" d="M23 181 H330 A65 65 0 0 1 395 246 V367 H88 A65 65 0 0 1 23 302 Z"/>
    <path class="callout-line" d="M53 201 H323 A52 52 0 0 1 375 253 V347 H105 A52 52 0 0 1 53 295 Z"/>
    <text class="heading" text-anchor="middle" font-size="19">
      <tspan x="209" y="257">INCREASING DEVELOPMENTAL</tspan>
      <tspan x="209" y="285">PRESSURES FROM RAPID</tspan>
      <tspan x="209" y="313">ECONOMIC GROWTH</tspan>
    </text>
  </g>

  <g class="pressure coordination">
    <path class="callout" d="M31 387 H288 A65 65 0 0 1 353 452 V962 H96 A65 65 0 0 1 31 897 Z"/>
    <path class="callout-line" d="M51 405 H280 A47 47 0 0 1 327 452 V946 H98 A47 47 0 0 1 51 899 Z"/>
    <text class="heading" text-anchor="middle" font-size="19">
      <tspan x="189" y="440">WEAK COORDINATION</tspan>
      <tspan x="189" y="468">BETWEEN MARINE</tspan>
      <tspan x="189" y="496">SECTORS</tspan>
    </text>
    <g class="sector-hexes body-text" font-size="12.5" text-anchor="middle">
      <g transform="translate(128 567)"><use href="#hexOuter" class="hex-cell"/><use href="#hexInner" class="hex-dash"/>
        <text y="-4">Coastal</text><text y="12">Tourism</text></g>
      <g transform="translate(257 567)"><use href="#hexOuter" class="hex-cell"/><use href="#hexInner" class="hex-dash"/>
        <text y="-12">Marine and</text><text y="4">Coastal</text><text y="20">Conservation</text></g>
      <g transform="translate(188 670)"><use href="#hexOuter" class="hex-cell"/><use href="#hexInner" class="hex-dash"/>
        <text y="-12">Navy and</text><text y="4">Marine</text><text y="20">Police</text></g>
      <g transform="translate(124 772)"><use href="#hexOuter" class="hex-cell"/><use href="#hexInner" class="hex-dash"/>
        <text y="-4">Marine</text><text y="12">Fisheries</text></g>
      <g transform="translate(254 773)"><use href="#hexOuter" class="hex-cell"/><use href="#hexInner" class="hex-dash"/>
        <text y="-12">Offshore Gas</text><text y="4">Exploration and</text><text y="20">Production</text></g>
      <g transform="translate(186 877)"><use href="#hexOuter" class="hex-cell"/><use href="#hexInner" class="hex-dash"/>
        <text y="-4">Maritime</text><text y="12">Transport</text></g>
    </g>
  </g>

  <g class="pressure ecosystems">
    <path class="callout" d="M390 776 H695 A65 65 0 0 1 760 841 V962 H455 A65 65 0 0 1 390 897 Z"/>
    <path class="callout-line" d="M420 796 H688 A52 52 0 0 1 740 848 V942 H472 A52 52 0 0 1 420 890 Z"/>
    <text class="heading" text-anchor="middle" font-size="19">
      <tspan x="573" y="853">DECLINING MARINE AND</tspan>
      <tspan x="573" y="881">COASTAL ECOSYSTEMS AND</tspan>
      <tspan x="573" y="909">RESOURCES</tspan>
    </text>
  </g>

  <!-- Flow arrows -->
  <g class="flows">
    <path class="flow-arrow" d="M562 70 Q650 70 690 125"/>
    <polygon class="flow-head" points="705,145 706,113 674,137"/>
    <path class="flow-arrow" d="M385 230 Q440 185 505 205"/>
    <polygon class="flow-head" points="529,212 510.8,185.8 499.2,224.2"/>
    <path class="flow-arrow" d="M362 650 Q420 655 430 612"/>
    <polygon class="flow-head" points="436,588 449.4,616.6 410.6,607.4"/>
    <path class="flow-arrow" d="M445 765 Q480 725 560 730"/>
    <polygon class="flow-head" points="584,731.5 558.8,750 561.2,710"/>
    <path class="flow-arrow" d="M1355 475 Q1395 545 1340 610"/>
    <polygon class="flow-head" points="1324,628 1355.4,623 1324.6,597"/>
  </g>

  <!-- Marine spatial planning cycle -->
  <g class="planning-cycle">
    <path class="seg-orange" d="M671.2 751.4 A300 300 0 0 1 509.5 239.3 L599.8 332.8 A170 170 0 0 0 691.5 623.0 Z"/>
    <path class="seg-stone" d="M509.5 239.3 A300 300 0 0 1 1004.8 367.4 L880.5 405.4 A170 170 0 0 0 599.8 332.8 Z"/>
    <path class="seg-green" d="M1004.8 367.4 A300 300 0 0 1 671.2 751.4 L691.5 623.0 A170 170 0 0 0 880.5 405.4 Z"/>

    <path class="tint-orange" d="M718 455 L691.5 623.0 A170 170 0 0 1 599.8 332.8 Z"/>
    <path class="tint-stone" d="M718 455 L599.8 332.8 A170 170 0 0 1 880.5 405.4 Z"/>
    <path class="tint-green" d="M718 455 L880.5 405.4 A170 170 0 0 1 691.5 623.0 Z"/>

    <circle class="seg-orange" cx="575" cy="283" r="32"/>
    <circle class="seg-stone" cx="910" cy="407" r="32"/>
    <circle class="seg-green" cx="665" cy="652" r="32"/>

    <text class="heading" font-size="22"><textPath href="#arcConsensus1" startOffset="53%" text-anchor="middle">CONSENSUS BUILDING</textPath></text>
    <text class="heading" font-size="22"><textPath href="#arcConsensus2" startOffset="50%" text-anchor="middle">AND CAPACITY DEVELOPMENT</textPath></text>
    <text class="heading" font-size="22"><textPath href="#arcInst1" startOffset="50%" text-anchor="middle">DEVELOPMENT OF</textPath></text>
    <text class="heading" font-size="22"><textPath href="#arcInst2" startOffset="50%" text-anchor="middle">INSTITUTIONAL ARRANGEMENTS</textPath></text>
    <text class="heading" font-size="22"><textPath href="#arcData" startOffset="50%" text-anchor="middle">DATA KNOWLEDGE STRENGTHENING</textPath></text>

    <text class="engage"><textPath href="#arcEngStone" startOffset="50%" text-anchor="middle">STAKEHOLDER ENGAGEMENT</textPath></text>
    <text class="engage"><textPath href="#arcEngOrange" startOffset="50%" text-anchor="middle">STAKEHOLDER ENGAGEMENT</textPath></text>
    <text class="engage"><textPath href="#arcEngGreen" startOffset="50%" text-anchor="middle">STAKEHOLDER ENGAGEMENT</textPath></text>

    <g class="cycle-arrows">
      <use href="#arcTop" class="cycle-band"/><use href="#arcTop" class="cycle-dash"/>
      <polygon class="cycle-head" points="786.9,397.1 817.6,371.4 815.1,403.4"/>
      <use href="#arcRight" class="cycle-band"/><use href="#arcRight" class="cycle-dash"/>
      <polygon class="cycle-head" points="733.7,543.6 740.6,583.1 714.2,564.9"/>
      <use href="#arcLeft" class="cycle-band"/><use href="#arcLeft" class="cycle-dash"/>
      <polygon class="cycle-head" points="633.4,424.2 595.8,410.5 624.7,396.7"/>
      <text class="heading" font-size="15" dominant-baseline="middle"><textPath href="#arcTop" startOffset="50%" text-anchor="middle">SHARED VISION</textPath></text>
      <text class="heading" font-size="15" dominant-baseline="middle"><textPath href="#arcRight" startOffset="50%" text-anchor="middle">COORDINATION</textPath></text>
      <text class="heading" font-size="15" dominant-baseline="middle"><textPath href="#arcLeft" startOffset="50%" text-anchor="middle">DECISION SUPPORT</textPath></text>
    </g>

    <circle class="hub" cx="718" cy="455" r="80"/>
    <text class="heading" text-anchor="middle" font-size="21">
      <tspan x="718" y="444">MARINE</tspan>
      <tspan x="718" y="473">SPATIAL</tspan>
      <tspan x="718" y="502">PLANNING</tspan>
    </text>
  </g>

  <!-- Adaptive management loop -->
  <g class="adaptive-loop">
    <path class="adapt-band" d="M1140 350 Q1085 305 1030 330"/>
    <polygon class="flow-head" points="1007,340 1039,350 1021,310"/>
    <path class="adapt-band" d="M1020 375 Q1070 420 1130 395"/>
    <polygon class="flow-head" points="1153,385.5 1138.4,415.2 1121.6,374.8"/>
    <text class="adapt-text" dominant-baseline="middle"><textPath href="#pathAdaptive" startOffset="50%" text-anchor="middle">ADAPTIVE</textPath></text>
    <text class="adapt-text" dominant-baseline="middle"><textPath href="#pathManagement" startOffset="50%" text-anchor="middle">MANAGEMENT</textPath></text>
  </g>

  <!-- National benefits Venn -->
  <g class="benefits">
    <text class="heading" font-size="32"><textPath href="#arcBenefits" startOffset="50%" text-anchor="middle">NATIONAL BENEFITS</textPath></text>
    <circle class="venn-env" cx="1295" cy="747" r="97"/>
    <circle class="venn-soc" cx="1130" cy="754" r="97"/>
    <circle class="venn-eco" cx="1212" cy="647" r="97"/>
    <circle class="venn-overlap" cx="1212" cy="647" r="97" clip-path="url(#clipSoc)"/>
    <circle class="venn-overlap" cx="1212" cy="647" r="97" clip-path="url(#clipEnv)"/>
    <circle class="venn-overlap" cx="1130" cy="754" r="97" clip-path="url(#clipEnv)"/>
    <circle class="venn-dash" cx="1212" cy="647" r="86"/>
    <circle class="venn-dash" cx="1130" cy="754" r="86"/>
    <circle class="venn-dash" cx="1295" cy="747" r="86"/>
    <g class="body-text" font-size="13" font-weight="600" text-anchor="middle">
      <text x="1212" y="621">ECONOMIC</text><text x="1212" y="637">VALUE</text>
      <text x="1130" y="745">SOCIAL</text><text x="1130" y="761">DEVELOPMENT</text>
      <text x="1297" y="747">ENVIRONMENTAL</text><text x="1297" y="763">SUSTAINABILITY</text>
    </g>
  </g>
</svg>
</body>
</html>
```